Veterinary hospital brochure design

we need brochure design for our veterinary hospital, something interesting, catchy and unique. Once we get going we need to add few unique services we offer and should be highlighted.Nice colors, and should be very professional looking. Brochure to be tri fold, nice colors highlight our services.
Like shades of blues or green.This is full service veterinary hospital. We do focus and specialize in Canine reproduction.

Target Market(s)

pet owners

Industry/Entity Type

Hospital

Font styles to use
Serif
Script

Requirements
Must have
• catchy words
• unique design
• have our unique services included
Nice to have
• good pictures and catchy words etc etc

```html
<!DOCTYPE html>
<html lang="en">
<head>
<meta charset="utf-8">
<title>Cedar Ridge Animal Hospital – Trifold Brochure</title>
<link rel="stylesheet" href="https://fonts.googleapis.com/css2?family=Lato:ital,wght@0,400;0,700;1,400&family=Roboto+Condensed:ital,wght@0,700;1,700&display=swap">
<style>
  :root {
    --blue: #1a86e0;
    --navy: #1c2a8c;
    --green: #9ccc1c;
    --ink: #2b2b2b;
    --grey: #6d6d6d;
    --paper: #ffffff;
    --backdrop: #e9ebee;
  }
  * { box-sizing: border-box; margin: 0; padding: 0; }
  html, body { width: 1200px; height: 1200px; overflow: hidden; }
  body { background: var(--backdrop); font-family: "Lato", sans-serif; color: var(--ink); }

  .brochure {
    position: absolute; left: 30px; top: 160px;
    width: 1140px; height: 880px;
    background: var(--paper);
    box-shadow: 0 6px 24px rgba(0,0,0,.15);
    overflow: hidden;
  }
  .fold { position: absolute; top: 0; bottom: 0; width: 1px; background: rgba(0,0,0,.08); }
  .fold--one { left: 380px; } .fold--two { left: 760px; }

  .swooshes { position: absolute; left: 0; top: 0; }

  .photo { position: absolute; }
  .photo--round { border-radius: 50%; border: 5px solid var(--navy); }

  .services { position: absolute; left: 40px; top: 40px; width: 320px; }
  .services__title {
    font-family: "Roboto Condensed", sans-serif; font-style: italic; font-weight: 700;
    color: var(--navy); font-size: 20px; letter-spacing: .5px; margin-bottom: 14px;
  }
  .services__list { list-style: none; }
  .services__item {
    display: flex; align-items: flex-start; gap: 10px;
    font-style: italic; font-size: 13px; line-height: 1.3; color: var(--ink);
    margin-bottom: 11px;
  }
  .services__icon { flex: none; width: 20px; height: 20px; }

  .testimonials { position: absolute; left: 410px; top: 40px; width: 320px; }
  .quote { font-style: italic; font-size: 13px; line-height: 1.45; margin-bottom: 16px; position: relative; padding-left: 14px; }
  .quote::before { content: "\201C"; position: absolute; left: -2px; top: -6px; font-size: 26px; font-weight: 700; color: var(--ink); }
  .quote__author { display: block; text-align: right; margin-top: 4px; }

  .contact { position: absolute; left: 410px; top: 610px; width: 330px; }
  .brand { display: flex; align-items: center; gap: 10px; margin-bottom: 22px; }
  .brand__mark { width: 14px; height: 14px; border-radius: 50%; background: var(--navy); flex: none; }
  .brand__name { font-size: 18px; font-weight: 400; color: var(--grey); letter-spacing: 1.5px; text-transform: uppercase; }
  .contact__name {
    font-family: "Roboto Condensed", sans-serif; font-weight: 700; font-size: 18px;
    text-transform: uppercase; margin-bottom: 8px;
  }
  .contact__row { display: flex; align-items: flex-start; gap: 8px; font-size: 14px; line-height: 1.35; margin-bottom: 4px; }
  .contact__icon { width: 14px; height: 14px; flex: none; margin-top: 2px; }

  .cover-brand { position: absolute; left: 800px; top: 70px; width: 310px; }
  .headline {
    position: absolute; left: 790px; top: 705px; width: 330px; color: #fff;
    font-family: "Roboto Condensed", sans-serif; font-weight: 700; text-transform: uppercase;
  }
  .headline__main { display: block; font-size: 36px; line-height: 1.05; letter-spacing: 1px; }
  .headline__sub { display: block; font-size: 21px; line-height: 1.3; letter-spacing: 1px; }
  .cover-url { position: absolute; left: 800px; top: 850px; font-size: 15px; font-weight: 700; color: var(--ink); }
</style>
</head>
<body>
<main class="brochure">

  <svg class="swooshes" width="1140" height="880" viewBox="0 0 1140 880" aria-hidden="true">
    <path d="M0,780 C120,700 260,520 420,475 C560,445 680,440 760,400 L760,425 C680,462 560,470 420,500 C270,545 130,720 0,810 Z" fill="var(--blue)"/>
    <path d="M0,832 C130,742 280,572 420,517 C560,487 690,482 770,447" fill="none" stroke="var(--green)" stroke-width="4"/>
    <path d="M830,0 C800,120 800,260 780,360 C770,420 760,470 760,520" fill="none" stroke="var(--navy)" stroke-width="6"/>
    <path d="M815,0 C785,120 785,260 766,360" fill="none" stroke="var(--green)" stroke-width="4"/>
  </svg>

  <div class="photo" role="img" aria-label="Veterinary technician in navy scrubs holding a senior beagle"
       style="left:30px;top:430px;width:310px;height:450px;background:linear-gradient(160deg,#b98a5c 0%,#2f3a6a 60%,#8a6a4c 100%);border-radius:40px 40px 0 0;"></div>

  <div class="photo" role="img" aria-label="Golden retriever sitting and smiling"
       style="left:900px;top:240px;width:230px;height:420px;background:radial-gradient(ellipse at 50% 45%,#d9862e 0%,#c77420 55%,#f6efe6 100%);border-radius:110px 110px 40px 40px;"></div>

  <svg class="swooshes" width="1140" height="880" viewBox="0 0 1140 880" aria-hidden="true">
    <path d="M760,560 C830,610 920,650 1000,668 C1060,680 1110,700 1140,720 L1140,820 C1080,810 900,825 760,840 Z" fill="var(--blue)"/>
    <path d="M760,548 C830,598 920,640 1000,658 C1060,670 1110,690 1140,708" fill="none" stroke="var(--navy)" stroke-width="5"/>
    <path d="M760,538 C830,588 920,630 1000,648 C1060,660 1110,680 1140,698" fill="none" stroke="var(--green)" stroke-width="4"/>
  </svg>

  <div class="photo photo--round" role="img" aria-label="Map showing the hospital's location"
       style="left:470px;top:330px;width:200px;height:200px;background:linear-gradient(135deg,#eceae4,#dcdad2);box-shadow:0 0 0 5px var(--green);"></div>
  <div class="photo photo--round" role="img" aria-label="Tabby cat with open mouth"
       style="left:770px;top:270px;width:140px;height:140px;background:radial-gradient(circle,#b59a72,#6e5a3e);"></div>
  <div class="photo photo--round" role="img" aria-label="Happy mixed-breed dog"
       style="left:755px;top:420px;width:125px;height:125px;background:radial-gradient(circle,#c9a27a,#7c5a3a);"></div>

  <div class="fold fold--one"></div>
  <div class="fold fold--two"></div>

  <section class="services">
    <h2 class="services__title">OUR SERVICES</h2>
    <ul class="services__list">
      <li class="services__item"><svg class="services__icon" viewBox="0 0 20 20"><circle cx="10" cy="10" r="10" fill="var(--blue)"/><path d="M5.5 10.5l3 3 6-6.5" fill="none" stroke="#fff" stroke-width="2"/></svg>Complete wellness examinations</li>
      <li class="services__item"><svg class="services__icon" viewBox="0 0 20 20"><circle cx="10" cy="10" r="10" fill="var(--blue)"/><path d="M5.5 10.5l3 3 6-6.5" fill="none" stroke="#fff" stroke-width="2"/></svg>Vaccines and health certificates</li>
      <li class="services__item"><svg class="services__icon" viewBox="0 0 20 20"><circle cx="10" cy="10" r="10" fill="var(--blue)"/><path d="M5.5 10.5l3 3 6-6.5" fill="none" stroke="#fff" stroke-width="2"/></svg>On-site laboratory for immediate blood and urine results</li>
      <li class="services__item"><svg class="services__icon" viewBox="0 0 20 20"><circle cx="10" cy="10" r="10" fill="var(--blue)"/><path d="M5.5 10.5l3 3 6-6.5" fill="none" stroke="#fff" stroke-width="2"/></svg>Radiology suite with automatic processor</li>
      <li class="services__item"><svg class="services__icon" viewBox="0 0 20 20"><circle cx="10" cy="10" r="10" fill="var(--blue)"/><path d="M5.5 10.5l3 3 6-6.5" fill="none" stroke="#fff" stroke-width="2"/></svg>Onsite ultrasound, endoscopy, dentistry and intensive/critical care unit</li>
      <li class="services__item"><svg class="services__icon" viewBox="0 0 20 20"><circle cx="10" cy="10" r="10" fill="var(--blue)"/><path d="M5.5 10.5l3 3 6-6.5" fill="none" stroke="#fff" stroke-width="2"/></svg>Surgical laser for all routine and specialized surgery</li>
      <li class="services__item"><svg class="services__icon" viewBox="0 0 20 20"><circle cx="10" cy="10" r="10" fill="var(--blue)"/><path d="M5.5 10.5l3 3 6-6.5" fill="none" stroke="#fff" stroke-width="2"/></svg>Pharmaceutical and pet supplies</li>
      <li class="services__item"><svg class="services__icon" viewBox="0 0 20 20"><circle cx="10" cy="10" r="10" fill="var(--blue)"/><path d="M5.5 10.5l3 3 6-6.5" fill="none" stroke="#fff" stroke-width="2"/></svg>Reproduction services</li>
      <li class="services__item"><svg class="services__icon" viewBox="0 0 20 20"><circle cx="10" cy="10" r="10" fill="var(--blue)"/><path d="M5.5 10.5l3 3 6-6.5" fill="none" stroke="#fff" stroke-width="2"/></svg>Boarding and Overnight Boarding</li>
      <li class="services__item"><svg class="services__icon" viewBox="0 0 20 20"><circle cx="10" cy="10" r="10" fill="var(--blue)"/><path d="M5.5 10.5l3 3 6-6.5" fill="none" stroke="#fff" stroke-width="2"/></svg>Grooming Services</li>
    </ul>
  </section>

  <section class="testimonials">
    <p class="quote">Our pets truly become part of our family. Just like with any family member, when they are not well it can create fear and anxiety (for the owner). The caring staff at Cedar Ridge do as much as possible, to assure peace of mind.<span class="quote__author">Dan Meyers</span></p>
    <p class="quote">The staff is always pleasant and accommodating. Even with urgent matters. They always do their best to see my cat right away when his condition becomes acute. Doctor Hale makes himself available all of the time and it is greatly appreciated.<span class="quote__author">Anonymous</span></p>
  </section>

  <section class="contact">
    <div class="brand"><span class="brand__mark"></span><span class="brand__name">Cedar Ridge</span></div>
    <h3 class="contact__name">Cedar Ridge Animal Hospital</h3>
    <p class="contact__row"><svg class="contact__icon" viewBox="0 0 14 14"><path d="M7 1a4 4 0 0 1 4 4c0 3-4 8-4 8S3 8 3 5a4 4 0 0 1 4-4z" fill="var(--navy)"/><circle cx="7" cy="5" r="1.5" fill="#fff"/></svg><span>48 Birchwood Lane<br>Fairhaven, CT 06512</span></p>
    <p class="contact__row"><svg class="contact__icon" viewBox="0 0 14 14"><path d="M3 1l2 0 1 3-1.5 1a7 7 0 0 0 4.5 4.5L10 8l3 1v2c0 1-1 2-2 2C6 13 1 8 1 3c0-1 1-2 2-2z" fill="var(--navy)"/></svg><span>(203) 555-0147</span></p>
    <p class="contact__row"><svg class="contact__icon" viewBox="0 0 14 14"><rect x="1" y="3" width="12" height="8" rx="1" fill="none" stroke="var(--navy)" stroke-width="1.4"/><path d="M1 3l6 5 6-5" fill="none" stroke="var(--navy)" stroke-width="1.4"/></svg><span>hello@cedarridgeanimal.com</span></p>
    <p class="contact__row"><svg class="contact__icon" viewBox="0 0 14 14"><circle cx="7" cy="7" r="6" fill="none" stroke="var(--navy)" stroke-width="1.4"/><path d="M1 7h12M7 1c-3 3-3 9 0 12M7 1c3 3 3 9 0 12" fill="none" stroke="var(--navy)" stroke-width="1.1"/></svg><span>www.cedarridgeanimal.com</span></p>
  </section>

  <div class="brand cover-brand"><span class="brand__mark"></span><span class="brand__name">Cedar Ridge Animal Hospital</span></div>

  <h1 class="headline">
    <span class="headline__main">Keeping your pet</span>
    <span class="headline__sub">On the path to wellness</span>
  </h1>
  <p class="cover-url">www.cedarridgeanimal.com</p>
</main>
</body>
</html>
```